K7 Digital Stationery Design Project

We are looking to have stationary designs created for our company branding materials. We are looking for the following to be created.
1. Business Cards (front & back)
2. Letterhead
3. Envelopes #10
We are a new web design, development and marketing firm. Primary color scheme is desired to be blue/grey/white. This web start-up is owned and operated by individuals with 15+ years experience each in the industry so should not look as though it is a start-up by young/inexperienced individuals.
We build website & custom applications/software. In addition we provide the full spectrum of web marketing solutions including SEO, PPC, Social Media, Branding, Content Marketing and PR.
Please let us know if you have any questions. Looking forward to seeing all the amazing design ideas.
Attached is our logo.
Thanks!
Target Market(s)
Company will be nearly 100% business to business sales. Looking to work with companies that are already established, with a website, who want to take their website and/or online marketing efforts to the next level.
Industry/Entity Type
Marketing
Look and feel

```html
<!DOCTYPE html>
<html lang="en">
<head>
<meta charset="utf-8">
<title>K7 Digital Stationery</title>
<link rel="stylesheet" href="https://fonts.googleapis.com/css2?family=Jost:wght@400;500;600&family=Arimo:wght@400&display=swap">
<style>
  :root {
    --backdrop: #e6e6e6;
    --paper: #ffffff;
    --brand-blue: #1696d4;
    --brand-blue-deep: #0b7cc2;
    --band-blue: #1a74bf;
    --ink-navy: #1c2a48;
    --ink-body: #2a2a2a;
    --ink-muted: #6b7583;
    --on-blue: #ffffff;
  }
  * { box-sizing: border-box; margin: 0; padding: 0; }
  html, body { width: 1200px; height: 800px; overflow: hidden; background: var(--backdrop); }
  .canvas { position: relative; width: 1200px; height: 800px; }
  .sheet { position: absolute; background: var(--paper); overflow: hidden; }

  .wordmark { font-family: "Jost", sans-serif; font-weight: 600; color: var(--ink-navy); letter-spacing: 0.02em; white-space: nowrap; display: flex; align-items: center; gap: 3px; }
  .wordmark .mark-dot { display: inline-block; background: var(--brand-blue); border-radius: 50%; }
  .tagline { font-family: "Jost", sans-serif; font-weight: 400; color: var(--ink-muted); white-space: nowrap; }

  .contact { font-family: "Jost", sans-serif; color: var(--on-blue); line-height: 1.25; }
  .contact .label { color: #bfe3f7; }

  /* Letterhead */
  .letterhead { left: 261px; top: 192px; width: 307px; height: 433px; }
  .letterhead .header-band { position: absolute; left: 0; top: 12px; width: 307px; height: 61px; background: linear-gradient(90deg, var(--brand-blue), var(--brand-blue-deep)); }
  .letterhead .logo-plate { position: absolute; left: 32px; top: 12px; width: 87px; height: 61px; background: var(--paper); display: flex; flex-direction: column; align-items: center; justify-content: flex-end; padding-bottom: 6px; }
  .letterhead .logo-plate .wordmark { font-size: 10px; }
  .letterhead .logo-plate .mark-dot { width: 7px; height: 7px; }
  .letterhead .logo-plate .tagline { font-size: 3.6px; margin-top: 1px; }
  .letterhead .contact { position: absolute; left: 139px; top: 19px; font-size: 7.4px; }
  .letterhead .contact .address { margin-bottom: 8px; }
  .letter-body { position: absolute; left: 33px; top: 90px; width: 259px; font-family: "Arimo", sans-serif; font-size: 5.3px; line-height: 10.5px; color: var(--ink-body); text-align: justify; }
  .letter-body p { margin-bottom: 4.5px; }
  .letter-body .salutation { margin-bottom: 6px; }
  .signature { display: block; width: 90px; height: 24px; margin: 4px 0 2px; background: linear-gradient(90deg, rgba(40,40,40,0.12), rgba(40,40,40,0.04)); }
  .signer { margin-left: 45px; line-height: 8px; }
  .letterhead .site { position: absolute; right: 23px; top: 406px; font-family: "Jost", sans-serif; font-size: 8.5px; color: var(--ink-navy); }
  .letterhead .footer-band { position: absolute; left: 0; bottom: 0; width: 307px; height: 12px; background: var(--band-blue); }

  /* Business card front */
  .card-front { left: 598px; top: 303px; width: 132px; height: 75px; }
  .card-front .pattern-fill { position: absolute; inset: 0; background: linear-gradient(160deg, #2ea4dd, #0d79c0); }
  .card-front .center { position: absolute; inset: 0; display: flex; flex-direction: column; align-items: center; justify-content: center; padding-top: 6px; }
  .card-front .wordmark { font-size: 8.5px; color: var(--on-blue); }
  .card-front .mark-dot { width: 6px; height: 6px; background: var(--on-blue); }
  .card-front .site { font-family: "Jost", sans-serif; font-size: 4.3px; color: var(--on-blue); margin-top: 9px; }

  /* Business card back */
  .card-back { left: 785px; top: 302px; width: 132px; height: 76px; }
  .card-back .name { position: absolute; left: 60px; top: 17px; font-family: "Jost", sans-serif; font-size: 5.6px; color: var(--ink-navy); white-space: nowrap; }
  .card-back .name small { font-size: 3.6px; color: var(--ink-muted); }
  .card-back .info-band { position: absolute; left: 0; top: 24px; width: 132px; height: 29px; background: linear-gradient(90deg, var(--brand-blue), var(--brand-blue-deep)); }
  .card-back .logo-plate { position: absolute; left: 8px; top: 24px; width: 44px; height: 29px; background: var(--paper); display: flex; align-items: flex-end; justify-content: center; padding-bottom: 3px; }
  .card-back .wordmark { font-size: 5.2px; }
  .card-back .mark-dot { width: 4px; height: 4px; }
  .card-back .contact { position: absolute; left: 60px; top: 26px; font-size: 3.3px; line-height: 1.3; }
  .card-back .contact .gap { margin-bottom: 2px; }
  .card-back .site { position: absolute; left: 60px; top: 56px; font-family: "Jost", sans-serif; font-size: 4px; color: var(--ink-navy); }

  /* Envelope */
  .envelope { left: 593px; top: 400px; width: 332px; height: 156px; }
  .envelope .corner-block { position: absolute; left: 0; top: 10px; width: 22px; height: 60px; background: var(--brand-blue); }
  .envelope .logo-plate { position: absolute; left: 22px; top: 10px; width: 86px; height: 60px; display: flex; flex-direction: column; align-items: center; justify-content: flex-end; padding-bottom: 4px; }
  .envelope .wordmark { font-size: 10px; }
  .envelope .mark-dot { width: 7px; height: 7px; }
  .envelope .tagline { font-size: 3.6px; margin-top: 1px; }
  .envelope .contact { position: absolute; left: 117px; top: 22px; font-size: 6.6px; color: var(--ink-navy); line-height: 1.2; }
  .envelope .contact .address { margin-bottom: 7px; }
  .envelope .contact .label { color: var(--brand-blue); }
  .envelope .site { position: absolute; left: 24px; top: 137px; font-family: "Jost", sans-serif; font-size: 8.2px; color: var(--ink-navy); }
  .envelope .footer-band { position: absolute; left: 0; bottom: 0; width: 332px; height: 7px; background: var(--band-blue); }
</style>
</head>
<body>
<main class="canvas">

  <section class="sheet letterhead" aria-label="Letterhead">
    <div class="header-band"></div>
    <div class="logo-plate">
      <div class="wordmark"><span class="mark-dot"></span>K7 DIGITAL</div>
      <div class="tagline">Web Design, Development and Marketing</div>
    </div>
    <div class="contact">
      <div class="address">12 Harbor Lane, Suite 400,<br>Ashford, NC 27500</div>
      <div><span class="label">P:</span> +1 555 014 2200</div>
      <div><span class="label">F:</span> +1 555 014 2201</div>
      <div><span class="label">E:</span> john@k7digital.com</div>
    </div>
    <div class="letter-body">
      <p class="salutation">Dear Client,</p>
      <p>Lorem ipsum dolor sit amet, consectetur adipisicing elit, sed do eiusmod tempor incididunt ut labore et dolore magna aliqua. Ut enim ad minim veniam, quis nostrud exercitation ullamco laboris nisi ut aliquip ex ea commodo consequat. Duis aute irure dolor in reprehenderit in voluptate velit esse cillum dolore eu fugiat nulla pariatur. Excepteur sint occaecat cupidatat non proident, sunt in culpa qui officia deserunt mollit anim id est laborum.</p>
      <p>Lorem ipsum dolor sit amet, consectetur adipisicing elit, sed do eiusmod tempor incididunt ut labore et dolore magna aliqua. Ut enim ad minim veniam, quis nostrud exercitation ullamco laboris nisi ut aliquip ex ea commodo consequat. Duis aute irure dolor in reprehenderit in voluptate velit esse cillum dolore eu fugiat nulla pariatur. Excepteur sint occaecat cupidatat non proident, sunt in culpa qui officia deserunt mollit anim id est laborum.</p>
      <p>Lorem ipsum dolor sit amet, consectetur adipisicing elit, sed do eiusmod tempor incididunt ut labore et dolore magna aliqua. Ut enim ad minim veniam, quis nostrud exercitation ullamco laboris nisi ut aliquip ex ea commodo consequat. Duis aute irure dolor in reprehenderit in voluptate velit esse cillum dolore eu fugiat nulla pariatur. Excepteur sint occaecat cupidatat non proident, sunt in culpa qui officia deserunt mollit anim id est laborum.</p>
      <p>Lorem ipsum dolor sit amet, consectetur adipisicing elit, sed do eiusmod tempor incididunt ut labore et dolore magna aliqua. Ut enim ad minim veniam, quis nostrud exercitation ullamco laboris nisi ut aliquip ex ea commodo consequat. Duis aute irure dolor in reprehenderit in voluptate velit esse cillum dolore eu fugiat nulla pariatur. Excepteur sint occaecat cupidatat non proident, sunt in culpa qui officia deserunt mollit anim id est laborum.</p>
      <p>Lorem ipsum dolor sit amet, consectetur adipisicing elit, sed do eiusmod tempor incididunt ut labore et dolore magna aliqua. Ut enim ad minim veniam, quis nostrud exercitation ullamco laboris nisi ut aliquip ex ea commodo consequat. Duis aute irure dolor in reprehenderit in voluptate velit esse cillum dolore eu fugiat nulla pariatur. Excepteur sint occaecat cupidatat non proident, sunt in culpa qui officia deserunt mollit anim id est laborum.</p>
      <p>Yours Sincerely,</p>
      <span class="signature" role="img" aria-label="Handwritten signature of Daniel Reyes"></span>
      <div class="signer">Daniel Reyes<br>Executive manager</div>
    </div>
    <div class="site">www.k7digital.com</div>
    <div class="footer-band"></div>
  </section>

  <section class="sheet card-front" aria-label="Business card front">
    <div class="pattern-fill" role="img" aria-label="Repeating brand pattern in blue tones"></div>
    <div class="center">
      <div class="wordmark"><span class="mark-dot"></span>K7 DIGITAL</div>
      <div class="site">www.k7digital.com</div>
    </div>
  </section>

  <section class="sheet card-back" aria-label="Business card back">
    <div class="name">Marcus Hale <small>Manager</small></div>
    <div class="info-band"></div>
    <div class="logo-plate">
      <div class="wordmark"><span class="mark-dot"></span>K7 DIGITAL</div>
    </div>
    <div class="contact">
      <div class="gap">12 Harbor Lane, Suite 400,<br>Ashford, NC 27500</div>
      <div>+1 555 014 2200</div>
      <div>+1 555 014 2201</div>
      <div>marcus@k7digital.com</div>
    </div>
    <div class="site">www.k7digital.com</div>
  </section>

  <section class="sheet envelope" aria-label="Envelope">
    <div class="corner-block"></div>
    <div class="logo-plate">
      <div class="wordmark"><span class="mark-dot"></span>K7 DIGITAL</div>
      <div class="tagline">Web Design, Development and Marketing</div>
    </div>
    <div class="contact">
      <div class="address">12 Harbor Lane, Suite 400,<br>Ashford, NC 27500</div>
      <div><span class="label">P:</span> +1 555 014 2200</div>
      <div><span class="label">F:</span> +1 555 014 2201</div>
      <div><span class="label">E:</span> john@k7digital.com</div>
    </div>
    <div class="site">www.k7digital.com</div>
    <div class="footer-band"></div>
  </section>

</main>
</body>
</html>
```